El Molinete Postcard

Please refer to our site for inspiration - I know this is alot of info but ?

El Molinete Reception Hall
4187C Quillmont Rd, Benicia, CA 707-555-0142
www.El-Molinete.example

Located in Benicia, California, we are a new venue that can host a variety of events. We can provide an exceptional space for your next party, reception, quinceañera, birthday party, or meeting! We treat each client with respect and go out of our way to accommodate all of your needs and make your event a success. Conveniently located just off the 680/780 junction, El Molinete is located in a safe, well-lit area with a large private parking area.

The space comes prepared with everything you need to get your party started – chairs and tables with tablecloths, a well-equipped kitchen, and incredible decorations to set the perfect backdrop to your event! Rent just the Lounge for a more intimate get-together, or add the Main Hall for your large sit-down event.

Lounge – Beautiful 1,600 ft2 entry room featuring large living room with conversation sofa seating for 40+ Sound system  Pass-through bar with seating  Fully-equipped 200 ft2 kitchen with
4-burner gas stove, oven, large double sink, full-size refrigerator, 2 microwaves, and ice machine, plus lots of storage and counter space  Newly-remodeled Men’s and Women’s bathrooms

Main Hall – Spacious 24’x80’ room with seating for up to 160 people  2,000 ft2  72” round tables with chairs, each seating up to 8 guests  DJ stand and Sound system  Atmospheric lighting
_______________________________________
Pricing -
Daytime Parties
Available 8AM-2PM
4-hour minimum

Lounge and Kitchen Only
Fri - Sat - Sun : $80/hr
Mon - Thurs : $60/hr

All Areas: Lounge, Kitchen, Main Hall, and Backyard
Fri - Sat - Sun : $120/hr
Mon - Thurs : $100/hr
___________________________________________
Evening Events
Available 3PM-12AM
5-hour minimum

Lounge and Kitchen Only -
Fri - Sat - Sun : $100/hr
Mon - Thurs : $50/hr

Fri - Sat - Sun : $160/hr
Mon - Thurs : $75/hr
___________________________________________________
Looking for a different time frame, all-day rental, or other special request? Let us know!
We'd be happy to provide you with a custom quote for your event.

I am not going to mail this postcard - only a hand out I need info and pricing on back

This is a hand out - will not be mailed

Only need my text on back

• Text and pricing on back
• Vintage feel to it

```html
<!DOCTYPE html>
<html lang="en">
<head>
<meta charset="utf-8">
<title>El Molinete Reception Hall – Handout</title>
<link rel="stylesheet" href="https://fonts.googleapis.com/css2?family=Montserrat:ital,wght@0,400;0,500;0,600;1,400&family=Tinos&display=swap">
<style>
  :root {
    --paper: #ffffff;
    --ink: #111111;
    --rule: #222222;
    --lounge-warm: #b08a5c;
    --lounge-dark: #5a4634;
    --chair-warm: #c79a62;
    --chair-dark: #4a3a2d;
    --buffet-light: #e9e1d3;
    --buffet-dark: #7d6a55;
    --hall-warm: #8a6644;
    --hall-dark: #3a2a1e;
  }
  * { box-sizing: border-box; margin: 0; padding: 0; }
  html, body { width: 1200px; height: 776px; overflow: hidden; background: var(--paper); }
  body { font-family: "Montserrat", Arial, sans-serif; color: var(--ink); }

  .handout { position: relative; width: 1200px; height: 776px; background: var(--paper); }

  .photo-column { position: absolute; left: 19px; top: 19px; width: 250px; }
  .photo { display: block; width: 250px; margin-bottom: 9px; }
  .photo--lounge { height: 178px; background: linear-gradient(180deg, #d9c7a6 0%, var(--lounge-warm) 45%, var(--lounge-dark) 100%); }
  .photo--chairs { height: 177px; background: radial-gradient(circle at 50% 45%, #f2d7a8 0%, var(--chair-warm) 35%, var(--chair-dark) 100%); }
  .photo--buffet { height: 178px; background: linear-gradient(180deg, #4b3d30 0%, var(--buffet-dark) 30%, var(--buffet-light) 70%, #cfc3b0 100%); }
  .photo--hall { height: 178px; background: linear-gradient(180deg, var(--hall-dark) 0%, var(--hall-warm) 55%, #d8cfc2 100%); margin-bottom: 0; }

  .intro { position: absolute; left: 292px; top: 34px; width: 878px; }
  .brand-name { font-family: "Montserrat", Arial, sans-serif; font-weight: 500; font-size: 40px; line-height: 48px; color: var(--ink); letter-spacing: 0.5px; }
  .tagline { font-style: italic; font-size: 14px; margin: 4px 0 0 3px; letter-spacing: 0.6px; }

  .copy { font-size: 12.6px; line-height: 16.2px; text-align: justify; }
  .copy--lead { margin-top: 16px; }
  .section-title { font-weight: 600; text-decoration: underline; text-underline-offset: 2px; }
  .copy-block { margin-top: 16px; }

  .pricing { position: absolute; left: 352px; top: 432px; width: 734px; }
  .pricing-title { font-size: 19px; font-weight: 400; letter-spacing: 0.5px; padding-bottom: 2px; border-bottom: 1.5px solid var(--rule); }
  .pricing-columns { display: flex; margin-top: 11px; }
  .pricing-col { width: 386px; font-size: 12.6px; line-height: 16.2px; }
  .pricing-group { margin-bottom: 16px; }

  .footer { position: absolute; left: 293px; top: 682px; font-family: "Tinos", "Times New Roman", serif; color: var(--ink); }
  .footer-name { font-size: 22px; letter-spacing: 0.3px; }
  .footer-contact { display: flex; align-items: center; margin-top: 6px; font-size: 19.5px; }
  .divider { display: inline-block; width: 1.5px; height: 22px; background: var(--ink); margin: 0 22px; }
  .icon { width: 14px; height: 14px; margin-right: 12px; }
</style>
</head>
<body>
<main class="handout">
  <div class="photo-column">
    <div class="photo photo--lounge" role="img" aria-label="Photo of the entry lounge with sofas and large windows"></div>
    <div class="photo photo--chairs" role="img" aria-label="Photo of two armchairs beside a lamp in front of a floral wall panel"></div>
    <div class="photo photo--buffet" role="img" aria-label="Photo of a buffet table with flowers and food trays under pendant lights"></div>
    <div class="photo photo--hall" role="img" aria-label="Photo of the main hall set with round tables, white tablecloths and string lights"></div>
  </div>

  <section class="intro">
    <h1 class="brand-name">El Molinete</h1>
    <p class="tagline">receptions . parties . memories</p>

    <p class="copy copy--lead">Located in Benicia, California, we are a new venue that can host a variety of events. We can provide an exceptional space for your next party, reception, quinceañera, birthday party, or meeting! We treat each client with respect and go out of our way to accommodate all of your needs and make your event a success.</p>

    <p class="copy copy-block"><span class="section-title">Three Areas to Fit Any Size Party!</span></p>

    <div class="copy copy-block">
      <p class="section-title">Entry Lounge</p>
      <p>Beautiful 1,600 sq ft entry room featuring large living room with conversation sofa seating for 40 – Sound system – Pass-through bar with seating – &nbsp;Newly-remodeled Men’s and Women’s bathrooms.</p>
    </div>

    <div class="copy copy-block">
      <p class="section-title">Kitchen</p>
      <p>Fully-equipped 200 sq ft kitchen – 4-burner gas stove and oven – Large double sink – Full-size refrigerator – 2 microwaves – Ice machine – Lots of storage and counter space</p>
    </div>

    <div class="copy copy-block">
      <p class="section-title">Main Hall</p>
      <p>Spacious 24’x80’ room with seating for up to 160 people – 2,000 sq ft – 72” round tables with chairs, each seating up to 8 guests – DJ stand and Sound system – Atmospheric lighting.</p>
    </div>
  </section>

  <section class="pricing">
    <h2 class="pricing-title">PRICING</h2>
    <div class="pricing-columns">
      <div class="pricing-col">
        <div class="pricing-group">
          <p class="section-title">Daytime Parties</p>
          <p>Available 8AM-2PM</p>
          <p>4-hour minimum</p>
        </div>
        <div class="pricing-group">
          <p class="section-title">Lounge and Kitchen Only</p>
          <p>Fri - Sat - Sun : $80/hr</p>
          <p>Mon - Thurs : $60/hr</p>
        </div>
        <div class="pricing-group">
          <p class="section-title">All Areas: Lounge, Kitchen, Main Hall, and Backyard</p>
          <p>Fri - Sat - Sun : $120/hr</p>
          <p>Mon - Thurs : $100/hr</p>
        </div>
      </div>
      <div class="pricing-col">
        <div class="pricing-group">
          <p class="section-title">Evening Events</p>
          <p>Available 3PM-12AM</p>
          <p>5-hour minimum</p>
        </div>
        <div class="pricing-group">
          <p class="section-title">Lounge and Kitchen Only</p>
          <p>Fri - Sat - Sun : $100/hr</p>
          <p>Mon - Thurs : $50/hr</p>
        </div>
        <div class="pricing-group">
          <p class="section-title">All Areas: Lounge, Kitchen, Main Hall, and Backyard</p>
          <p>Fri - Sat - Sun : $160/hr</p>
          <p>Mon - Thurs : $75/hr</p>
        </div>
      </div>
    </div>
  </section>

  <footer class="footer">
    <p class="footer-name">EL MOLINETE RECEPTION HALL</p>
    <p class="footer-contact">
      <span>4187C Quillmont Rd, Benicia, CA</span>
      <span class="divider"></span>
      <svg class="icon" viewBox="0 0 24 24" aria-hidden="true"><path fill="currentColor" d="M6.6 10.8c1.4 2.8 3.8 5.1 6.6 6.6l2.2-2.2c.3-.3.7-.4 1-.2 1.1.4 2.3.6 3.6.6.6 0 1 .4 1 1V20c0 .6-.4 1-1 1C10.6 21 3 13.4 3 4c0-.6.4-1 1-1h3.5c.6 0 1 .4 1 1 0 1.3.2 2.5.6 3.6.1.3 0 .7-.2 1z"/></svg>
      <span>707-555-0142</span>
      <span class="divider"></span>
      <svg class="icon" viewBox="0 0 24 24" aria-hidden="true"><path fill="currentColor" d="M2 5h20v14H2z M4 7v.5l8 5.5 8-5.5V7z" fill-rule="evenodd"/></svg>
      <span>events@el-molinete.example</span>
    </p>
  </footer>
</main>
</body>
</html>
```